Medical Clinic Website Makeover

Our website needs a make over. We would like something appealing, modern, captivating and aesthetically pleasing for our medical practice.
The website must be informative whilst flowing with ease and also entice patients to explore the website.

It is essential that the website is compatible across all devices and user friendly, especially when it comes to updating details within the website etc.

Our current page is http://www.brightharbourclinic.com.au

Given the multiple locations of which we currently consult and operate from, our contact page should include a clear map outlining each clinic location.
- 48 Morrow Street Echuca VIC 3550
- 312 Tolley Street Bendigo Vic 3550
- Suite 5/47 Quarry Avenue Mildura VIC 3500
- Level 7, 418 Dunmore Street Melbourne Vic 3000
- 291 Oakvale Road, Cnr Harlow Road Bundoora VIC 3083

The pages to be included should be as follows:
Home
About
Our Clinic
Booking
ENT Conditions
Facial Plastics
Contact
Updates

Target Market(s)

Adults, Families

Coding

Coded - Design and coding required

Number of Pages Required

5+ page

Requirements
Must have
• Modern
Captivating
Aesthetically pleasing

Online booking page
Nice to have
• It would be great to have the option for instant chat for patients that have enquiries

A page for patients to make payments online would be amazing. Here is an example of another website that does this: https://tidewellcare.com.au/payment ( this MUST be secure)

```html
<!DOCTYPE html>
<html lang="en">
<head>
<meta charset="utf-8">
<title>Bright Harbour ENT</title>
<link href="https://fonts.googleapis.com/css2?family=Poppins:wght@300;400;500;600&display=swap" rel="stylesheet">
<style>
:root{
  --blue:#2c3f9f;
  --blue-deep:#24358c;
  --ink:#222433;
  --muted:#7b7f8e;
  --accent:#8e2fa8;
  --cyan:#2aa6d9;
  --orange:#f2a033;
  --pale:#f4f6fb;
  --footer:#252c45;
  --footer-text:#aeb4c8;
}
*{margin:0;padding:0;box-sizing:border-box}
html,body{width:1200px;height:4258px;overflow:hidden}
body{position:relative;font-family:'Poppins',sans-serif;color:var(--ink);background:var(--pale)}
.abs{position:absolute}
.center{text-align:center;left:0;width:1200px}

/* header */
.topbar{top:24px;right:52px;display:flex;gap:46px;font-size:19px;color:var(--blue);align-items:center}
.topbar .call{display:flex;gap:12px;align-items:center;font-size:21px}
.brand{top:62px;left:52px;display:flex;align-items:center;gap:14px}
.brand .dot{width:48px;height:48px;border-radius:50%;background:var(--blue)}
.brand span{font-size:33px;font-weight:500;color:var(--blue);letter-spacing:-.5px}
.nav{top:69px;left:440px;width:593px;height:68px;background:#fff;display:flex;align-items:center;justify-content:space-around;padding:0 20px;font-size:17px;font-weight:500}
.booking{top:69px;left:1033px;width:167px;height:68px;background:var(--blue);color:#fff;font-size:17px;font-weight:500;display:flex;align-items:center;justify-content:center}

/* hero */
.hero-photo{top:0;left:0;width:1200px;height:740px;background:linear-gradient(135deg,#dfe6ee 0%,#9fc0dc 40%,#5d8cbf 70%,#2f4e7c 100%)}
.hero-caption{top:412px;left:365px;width:470px;height:100px;background:rgba(40,44,60,.62);color:#fff;font-size:20px;text-align:center;padding-top:20px;line-height:30px}
.btn-primary{background:var(--blue);color:#fff;border-radius:26px;display:flex;align-items:center;justify-content:center;font-size:17px}

/* headings */
.kicker{font-size:14px;color:var(--muted);letter-spacing:.5px}
.title{font-size:43px;font-weight:300}
.rule{width:40px;height:3px;background:var(--accent);left:580px}

/* services */
.map-shade{top:860px;left:460px;width:640px;height:260px;border-radius:50%;background:radial-gradient(ellipse,#e6e9f2 0%,rgba(244,246,251,0) 70%)}
.svc{width:330px;text-align:center}
.svc-card{top:937px;left:119px;width:326px;height:304px;background:#fff;box-shadow:0 12px 30px rgba(40,50,90,.12)}
.svc h3{font-size:17px;font-weight:500;margin-top:20px}
.svc p{font-size:12.5px;color:var(--muted);line-height:23px;margin:22px auto 0;width:250px}

/* team */
.team{top:1494px;height:485px;width:400px;color:#fff;text-align:center}
.team .name{font-size:19px;font-weight:500}
.team .role{font-size:15px;line-height:23px;margin-top:12px}
.btn-light{background:#fff;color:var(--ink);border-radius:20px;width:136px;height:38px;margin:28px auto 0;display:flex;align-items:center;justify-content:center;font-size:15px}

/* first appointment */
.ap-title{font-size:42px;font-weight:300}
.ap-intro{font-size:15.5px;line-height:30px}
.item{font-size:15.5px;line-height:27px}
.tick{width:36px;height:36px}

/* contact band */
.band{top:2691px;left:0;width:1200px;height:232px;background:var(--blue);overflow:hidden}

/* form */
.form-area{top:2923px;left:0;width:1200px;height:560px;background:#fff}
.field{top:3179px;width:243px;height:39px;border:1px solid #dcdfe7;font-size:13px;color:#a0a4b0;padding:10px 18px}

/* footer */
.footer{top:3843px;left:0;width:1200px;height:415px;background:var(--footer);color:var(--footer-text)}
.fcol{top:89px;font-size:12.5px}
.fcol h4{color:#fff;font-size:14.5px;font-weight:600;margin-bottom:16px}
.fcol li{list-style:none;line-height:28px}
</style>
</head>
<body>

<!-- hero -->
<div class="abs hero-photo" role="img" aria-label="Surgical team in scrubs operating with a microscope in a theatre"></div>
<svg class="abs" style="top:560px;left:0" width="1200" height="200" viewBox="0 0 1200 200">
  <path d="M0 70 Q300 150 600 180 Q900 150 1200 70 L1200 200 L0 200Z" fill="#f4f6fb"/>
</svg>
<div class="abs hero-caption">BRIGHT HARBOUR ENT<br>EAR NOSE &amp; THROAT SURGEONS</div>
<div class="abs btn-primary" style="top:560px;left:489px;width:222px;height:45px">Get Appointment</div>

<div class="abs topbar">
  <span>Contact Us</span>
  <span class="call">Call
    <svg width="34" height="34" viewBox="0 0 24 24" fill="none" stroke="currentColor" stroke-width="1.3"><path d="M5 3h4l2 5-2.5 1.5a11 11 0 0 0 6 6L16 13l5 2v4a2 2 0 0 1-2 2A17 17 0 0 1 3 5a2 2 0 0 1 2-2z"/></svg>
    03 5590 2174</span>
</div>
<div class="abs brand"><div class="dot"></div><span>Bright Harbour ENT</span></div>
<nav class="abs nav"><span>About</span><span>Our Clinic</span><span>ENT Conditions</span><span>Facial Plastics</span></nav>
<div class="abs booking">Booking</div>

<!-- services -->
<div class="abs center kicker" style="top:792px">WHAT WE DO</div>
<div class="abs center title" style="top:820px">Our Services</div>
<div class="abs rule" style="top:886px"></div>
<div class="abs map-shade" role="img" aria-label="Faint dotted world map"></div>
<div class="abs svc-card"></div>

<div class="abs svc" style="top:985px;left:117px">
  <svg width="50" height="70" viewBox="0 0 50 70" fill="none" stroke="var(--blue)" stroke-width="2"><path d="M12 30a16 18 0 1 1 30 8c-4 6-8 8-8 16a8 8 0 0 1-16 0"/><path d="M20 30a7 8 0 1 1 13 4"/></svg>
  <h3>Ear Conditions</h3>
  <p>Glue ear is the commonest cause of hearing loss in children. It refers to thick fluid</p>
</div>
<div class="abs svc" style="top:985px;left:490px">
  <svg width="50" height="70" viewBox="0 0 50 70" fill="none" stroke="var(--blue)" stroke-width="2"><path d="M25 4c-2 16-14 30-14 40a8 8 0 0 0 10 8h8a8 8 0 0 0 10-8c0-10-12-24-14-40"/><circle cx="20" cy="46" r="3"/><circle cx="30" cy="46" r="3"/></svg>
  <h3>Nasal Conditions</h3>
  <p>The nose is responsible for 25% of breathing function and everyone knows what a blocked nose feels like.</p>
</div>
<div class="abs svc" style="top:985px;left:799px">
  <svg width="70" height="70" viewBox="0 0 70 70" fill="none" stroke="var(--blue)" stroke-width="2"><path d="M30 60V40l-6-4 8-12c0-12 8-18 18-18s14 8 14 18c0 8-6 12-6 20v16"/><path d="M4 30h14M6 38h12M4 46h14"/></svg>
  <h3>Throat Conditions</h3>
  <p>Mr Ellery has undertaken cancer surgery in the Head and Neck for more than 15 years</p>
</div>

<!-- team -->
<div class="abs center kicker" style="top:1348px">WHAT WE DO</div>
<div class="abs center title" style="top:1376px">Our Services</div>
<div class="abs rule" style="top:1441px"></div>

<div class="abs team" style="left:0;background:linear-gradient(180deg,#3446a6,#2b3d9c)" role="img" aria-label="Portrait of Dr Martin Ellery with blue overlay">
  <div style="margin-top:280px" class="name">Dr Martin Ellery</div>
  <div class="role">ENT, Head, Neck,<br>Facial Plastic Surgeon</div>
  <div class="btn-light">View Bio</div>
</div>
<div class="abs team" style="left:400px;background:linear-gradient(180deg,#8d96a8,#4a5060 60%,#1e2230)" role="img" aria-label="Portrait of Dr Martin Ellery in a dark suit">
  <div style="margin-top:300px" class="name">Dr Martin Ellery</div>
  <div class="role">Anaesthetist - Bright Harbour<br>Anaesthetic Services</div>
</div>
<div class="abs team" style="left:800px;background:linear-gradient(180deg,#9aa1ae,#4f4a52 60%,#2e3a86)" role="img" aria-label="Portrait of Tamsin Hollis">
  <div style="margin-top:300px" class="name">Tamsin Hollis</div>
  <div class="role">Personal Assistant to<br>Dr Martin Ellery</div>
</div>

<!-- first appointment -->
<div class="abs center ap-title" style="top:2066px">Your First Appointment</div>
<div class="abs center ap-intro" style="top:2136px">We want your experience with Bright Harbour ENT to be a good one. To make things easier,<br>please make sure you have the following with you.</div>

<svg class="abs" style="top:2270px;left:380px" width="440" height="260" viewBox="0 0 440 260">
  <circle cx="180" cy="132" r="127" fill="#e1ecf7"/>
  <circle cx="180" cy="132" r="94" fill="#c9def2"/>
  <g stroke="var(--cyan)" stroke-width="2.5">
    <line x1="12" y1="62" x2="104" y2="62"/><line x1="4" y1="208" x2="96" y2="208"/>
    <line x1="256" y1="62" x2="348" y2="62"/><line x1="264" y1="208" x2="356" y2="208"/>
  </g>
  <g fill="var(--cyan)"><circle cx="104" cy="62" r="5"/><circle cx="96" cy="208" r="5"/><circle cx="256" cy="62" r="5"/><circle cx="264" cy="208" r="5"/></g>
</svg>

<svg class="abs tick" style="top:2268px;left:180px" viewBox="0 0 36 36" fill="none" stroke="var(--ink)" stroke-width="2.2"><path d="M32 15A15 15 0 1 1 24 5"/><path d="M11 17l6 6L33 7"/></svg>
<div class="abs item" style="top:2308px;left:177px">Referral letter<br>from your GP</div>
<svg class="abs tick" style="top:2426px;left:180px" viewBox="0 0 36 36" fill="none" stroke="var(--ink)" stroke-width="2.2"><path d="M32 15A15 15 0 1 1 24 5"/><path d="M11 17l6 6L33 7"/></svg>
<div class="abs item" style="top:2466px;left:177px">Medicare Card or private<br>insurance details</div>
<svg class="abs tick" style="top:2268px;left:771px" viewBox="0 0 36 36" fill="none" stroke="var(--ink)" stroke-width="2.2"><path d="M32 15A15 15 0 1 1 24 5"/><path d="M11 17l6 6L33 7"/></svg>
<div class="abs item" style="top:2308px;left:767px">Physical copies of any imaging<br>(X-ray etc) or current tests</div>
<svg class="abs tick" style="top:2426px;left:771px" viewBox="0 0 36 36" fill="none" stroke="var(--ink)" stroke-width="2.2"><path d="M32 15A15 15 0 1 1 24 5"/><path d="M11 17l6 6L33 7"/></svg>
<div class="abs item" style="top:2466px;left:769px">Any other relevant doctors letters,<br>results etc, you may have.</div>

<!-- contact band -->
<div class="abs band">
  <div class="abs" style="top:62px;left:164px;color:#fff;font-size:22px;font-weight:300">Contact us</div>
  <div class="abs" style="top:100px;left:164px;color:#fff;font-size:38px;font-weight:300">Following a consultation</div>
  <div class="abs" style="top:96px;left:785px;width:156px;height:45px;border-radius:24px;background:#fff;color:var(--blue);font-size:16px;display:flex;align-items:center;justify-content:center">Contact Us</div>
</div>

<!-- enquiry form -->
<div class="abs form-area"></div>
<div class="abs center" style="top:3006px;font-size:32px;font-weight:300">We are always ahead</div>
<div class="abs center" style="top:3050px;font-size:31px;font-weight:600;color:#2c2f45">Professional Solutions for You</div>
<div class="abs center" style="top:3109px;font-size:20px;font-weight:300">I would like to discuss</div>
<div class="abs field" style="left:217px">Name</div>
<div class="abs field" style="left:478px">Email</div>
<div class="abs field" style="left:739px">Phone</div>
<div class="abs" style="top:3256px;left:534px;width:131px;height:45px;background:var(--blue);color:#fff;font-size:16px;display:flex;align-items:center;justify-content:center">Submit</div>

<!-- testimonials -->
<svg class="abs" style="top:3340px;left:0" width="1200" height="510" viewBox="0 0 1200 510">
  <path d="M0 230 C200 140 300 20 600 40 C850 60 950 140 1200 90 L1200 510 L0 510Z" fill="var(--pale)"/>
  <path d="M0 230 C200 140 300 20 600 40 C850 60 950 140 1200 90 L1200 0 L0 0Z" fill="#fff"/>
</svg>
<div class="abs center" style="top:3460px;font-size:14.5px">Our Customer Says</div>
<div class="abs center" style="top:3484px;font-size:31px;font-weight:600;color:#2c2f45">Testimonials</div>
<div class="abs" style="top:3540px;left:570px;width:60px;height:3px;background:linear-gradient(90deg,var(--cyan),var(--orange))"></div>
<div class="abs" style="top:3578px;left:344px;width:124px;height:124px;border-radius:50%;background:#dde9e6"></div>
<div class="abs" style="top:3582px;left:344px;width:116px;height:116px;border-radius:50%;background:linear-gradient(160deg,#e6e2de,#6b5a55 70%,#2b3a6e)" role="img" aria-label="Portrait of customer Nadia Welling"></div>
<div class="abs" style="top:3622px;left:336px;width:34px;height:34px;border-radius:50%;background:var(--orange);color:#fff;font-size:20px;text-align:center;line-height:38px;font-weight:600">&ldquo;</div>
<div class="abs" style="top:3590px;left:511px;font-size:15.5px;line-height:33px;color:#6b6f7e">This is due to their excellent service, competitive<br>pricing and customer support. It's throughly refresing<br>to get such a personal touch.</div>
<div class="abs" style="top:3713px;left:511px;font-size:14.5px;font-weight:500;color:var(--cyan)">Nadia Welling</div>
<svg class="abs" style="top:3752px;left:890px" width="64" height="18" viewBox="0 0 64 18" fill="none" stroke-width="1.6"><path d="M26 9H2M9 2L2 9l7 7" stroke="var(--cyan)"/><path d="M36 9h24M53 2l7 7-7 7" stroke="#9aa0b0"/></svg>

<!-- footer -->
<footer class="abs footer">
  <div class="abs fcol" style="left:117px">
    <h4>Contact Us</h4>
    <div style="display:flex;gap:12px;line-height:22px;margin-top:8px"><svg width="16" height="20" viewBox="0 0 16 20" fill="none" stroke="#fff" stroke-width="1.4"><path d="M8 19s6-6 6-11A6 6 0 0 0 2 8c0 5 6 11 6 11z"/><circle cx="8" cy="8" r="2"/></svg><span>82 Linden Row #4B<br>Texas 10031 TX</span></div>
    <div style="display:flex;gap:12px;margin-top:18px;color:#fff;font-size:14px"><svg width="18" height="18" viewBox="0 0 24 24" fill="none" stroke="#fff" stroke-width="1.6"><path d="M5 3h4l2 5-2.5 1.5a11 11 0 0 0 6 6L16 13l5 2v4a2 2 0 0 1-2 2A17 17 0 0 1 3 5a2 2 0 0 1 2-2z"/></svg>(123) 555 0148</div>
    <div style="display:flex;gap:12px;margin-top:20px"><svg width="18" height="14" viewBox="0 0 18 14" fill="none" stroke="#fff" stroke-width="1.3"><rect x="1" y="1" width="16" height="12"/><path d="M1 1l8 7 8-7"/></svg>hello@brightharbourclinic.com.au</div>
  </div>
  <div class="abs fcol" style="left:410px"><h4>Quick Links</h4><ul><li>Home</li><li>Oor Clinic</li><li>ENT Conditions</li><li>Facial Plastics</li><li>Bookin</li></ul></div>
  <div class="abs fcol" style="left:560px"><h4>Quick Links</h4><ul><li>Support</li><li>Testimonials</li><li>Sitemap</li><li>Career</li><li>Contact Us</li></ul></div>
  <div class="abs fcol" style="left:760px"><h4>WRITE TO US</h4><div style="font-size:11.5px;line-height:24px">Provide your email below to<br>subscribe to our newsletter</div></div>
  <div class="abs" style="top:182px;left:750px;width:329px;height:36px;border-radius:18px;background:#fff;display:flex;overflow:hidden;font-size:13px">
    <span style="flex:1;padding:9px 22px;color:#9aa0b0">Email address</span>
    <span style="width:118px;background:var(--cyan);color:#fff;display:flex;align-items:center;justify-content:center">Subscribe</span>
  </div>
  <div class="abs" style="top:308px;left:0;width:1200px;height:1px;background:#343c58"></div>
  <div class="abs" style="top:350px;left:117px;font-size:12.5px">Copyright 2020 brightharbourclinic.com.au</div>
  <div class="abs" style="top:341px;left:520px;display:flex;gap:10px;align-items:center"><span style="width:22px;height:22px;border-radius:50%;background:var(--blue)"></span><span style="color:#5b6bc0;font-size:20px;font-weight:500">Bright Harbour ENT</span></div>
  <div class="abs" style="top:353px;left:953px;display:flex;gap:12px">
    <span style="width:10px;height:10px;border-radius:50%;background:var(--footer-text)"></span>
    <span style="width:10px;height:10px;border-radius:50%;background:var(--footer-text)"></span>
    <span style="width:10px;height:10px;border-radius:50%;background:var(--footer-text)"></span>
    <span style="width:10px;height:10px;border-radius:50%;background:var(--footer-text)"></span>
    <span style="width:10px;height:10px;border-radius:50%;background:var(--footer-text)"></span>
  </div>
</footer>

</body>
</html>
```